Hi,

I would like to have a invitation made for a party. exactly like the picture in the link below.

http://pinboardia.example/pin/730215948361027459/

However, Please change the colors into fun/ girly feeling. font can be different and size of the card should be the same

Name of the girl: RINA
What: Bachelorette Party
Where:TOLO Boat
Dubai Coral Quay Sailing Club
When:7th of February 2013

No RSVP required. (so no need to put it)

```html
<!DOCTYPE html>
<html lang="en">
<head>
<meta charset="utf-8">
<title>Rina's Bachelorette Invitation</title>
<link rel="stylesheet" href="https://fonts.googleapis.com/css2?family=Rye&family=Ewert&family=Parisienne&display=swap">
<style>
  :root {
    --canvas: #ffffff;
    --card-bg: #fdf3f3;
    --card-edge: #9a9a9a;
    --ink-brown: #6b2b38;
    --ink-plum: #8c1c4e;
    --ornament: #7a3a46;
    --ornament-soft: #c9a3ab;
  }
  * { margin: 0; padding: 0; box-sizing: border-box; }
  html, body {
    width: 1200px;
    height: 900px;
    overflow: hidden;
    background: var(--canvas);
  }
  .invitation {
    position: absolute;
    left: 110px;
    top: 224px;
    width: 954px;
    height: 460px;
    background: var(--card-bg);
    border: 1px solid var(--card-edge);
  }
  .ornament {
    position: absolute;
    background: radial-gradient(circle, var(--ornament) 0%, var(--ornament-soft) 60%, transparent 72%);
    opacity: 0.55;
  }
  .ornament--top-left { left: 240px; top: 12px; width: 64px; height: 64px; }
  .ornament--bottom-left { left: 10px; top: 364px; width: 70px; height: 70px; }
  .ornament--divider {
    left: 370px; top: 78px; width: 180px; height: 40px;
    background: linear-gradient(90deg, transparent, var(--ornament-soft) 25%, var(--ornament) 50%, var(--ornament-soft) 75%, transparent);
    border-radius: 50%;
    opacity: 0.5;
  }
  .headline {
    position: absolute;
    left: 10px;
    top: 84px;
    width: 620px;
  }
  .headline__name {
    font-family: "Rye", serif;
    font-size: 56px;
    line-height: 1;
    color: var(--ink-brown);
    letter-spacing: 1px;
  }
  .headline__tagline {
    font-family: "Parisienne", cursive;
    font-size: 44px;
    line-height: 1.05;
    color: var(--ink-brown);
    margin-top: 6px;
    white-space: nowrap;
  }
  .headline__single {
    font-family: "Ewert", serif;
    font-size: 150px;
    line-height: 1;
    color: var(--ink-plum);
    letter-spacing: 2px;
    margin-top: -4px;
  }
  .details {
    position: absolute;
    left: 650px;
    top: 16px;
    width: 290px;
    height: 416px;
    border: 3px solid var(--ink-brown);
    border-radius: 18px;
    text-align: center;
    padding-top: 38px;
  }
  .details__label {
    font-family: "Rye", serif;
    font-size: 26px;
    color: var(--ink-plum);
    line-height: 1;
  }
  .details__value {
    font-family: "Parisienne", cursive;
    font-size: 24px;
    color: var(--ink-brown);
    line-height: 1.9;
    margin-top: 6px;
  }
  .details__item + .details__item { margin-top: 26px; }
</style>
</head>
<body>
  <main class="invitation">
    <div class="ornament ornament--top-left" role="img" aria-label="Small scrolled flourish ornament"></div>
    <div class="ornament ornament--bottom-left" role="img" aria-label="Small scrolled flourish ornament"></div>
    <div class="ornament ornament--divider" role="img" aria-label="Decorative scroll divider with fleur centre"></div>

    <header class="headline">
      <h1 class="headline__name">RINA'S</h1>
      <p class="headline__tagline">Last Chance to Celebrate Being</p>
      <p class="headline__single">SINGLE</p>
    </header>

    <section class="details">
      <div class="details__item">
        <h2 class="details__label">WHAT:</h2>
        <p class="details__value">Bachelorette Party</p>
      </div>
      <div class="details__item">
        <h2 class="details__label">WHERE:</h2>
        <p class="details__value">TOLO Boat Dubai Coral Quay<br>Sailing Club</p>
      </div>
      <div class="details__item">
        <h2 class="details__label">WHEN:</h2>
        <p class="details__value">7th of February 2013</p>
      </div>
    </section>
  </main>
</body>
</html>
```